Lumo Throw Co Website Shopi

Mobile Responsive Shopify Website
logo: https://www.artboardhub.example/design/58104927
Welcome to LuMo + (The What )
Lumo + Throw Co is the original and only “scented” luxury & travel blanket company in the world introducing refillable infused and scented LuMo pearls (TM) Patent pending (ceramic beads) and Lumo “BRISK” cards (TM) combined with essential oils with medicinal life giving benefits .

LuMo has pioneered the “wellness blanket” category and distribute globally via ecommerce from our website www.lumothrows.example and through select licensing partners including collections and collaborations from top designers , micro influencers , lifestyle and wellness distributors and retailers .

Our mission is to deliver a sensory and wellness “experience” that transcends time and takes you away to wrap you in warmth, chic and function. To all the dreamers , seekers , caretakers, healers, wanderers , poets, nomads, romanticists , Bohemians , travel obsessed , we salute you . All you vision quest journey people . Calling all Human BEings . To the “think different” generation , you rebels with a cause / humanitarian and philanthropic change agents I see and feel you ! . You are a unique force in the universe and deserve to Live your dreams with passion with “good LuMo energy .

The birth of LUMO + == In a general sense, the term can be used to refer to magical and supernatural properties and powers dealing with good luck.

The Who - Our Story )

Founded and inspired by Mirela aka “LUMO” Brandeis Kettering affectionately know by her hubby as “Super M “ , Mirela was nicknamed Lumo at birth and her brothers teased her to tears in her formative years giving her the nickname Lumo Pemberton . A college graduate in Health and wellness , fast forward, 5 kids later , Mirel now travels the world as a top travel influencer and consultant agent with Roams and Rafts luxury Travel www.Roamsandrafts.example . She blends artistry with dreamscaping and is everybody’s “good vibes” best friend and loyal confidant . Known for her positive energy as “the Travel Poet” her childhood nickname has come full circle ironically as she is passionate about creating powerful bonds while curating atmosphere and crafting experiences and memories that transcend time . A true world traveler and renaissance woman and thinker ,
Lumo Throw Co + is a representation of her true “essence “ and lifelong dream of health and wellness mixed with luxury couture and travel .

Lumo is the first blanket company in the world to blend and infuse the sights , feeling and fragrances of foreign lands and “Mother Earth “ made from the elements and properties of some of the finest materials , fabrics , minerals and oils from around the world. We bring it HOME to YOU in pure cozy luxury couture .

current logo: https://www.artboardhub.example/design/58102291
Reference Websites:
Www.Penacovers.example
Www.velvetrishaus.example
Www.roamsandrafts.example
Updates

Designers

So far.....l
I’m not very impressed with the lack of creativity in design and dreamscaping so im hoping to be more specific . We are looking for some "wow factor" and artistry. So far we have had all static pics with no imagination and I gave 3 samples with dynamic shots and video versus static pics . I would like to tell a story of senses and international travel tapping into beautiful scapes and Mother Earth. We also want to animate the logo as if someone was handwriting it and have consistency in the font headers but the body content i provided in the brief scope please insert the copy . Go to some hotel sites on YouTube like this one called "ORBITude – Let the quiet hold you near " and use it and the music for now . This is a sensory experience including oils, scents and luxury in the form of a blanket where we encapsulate the frangrances and tell a story. Also please change the font to the most used and up to date modern .

So far these pics of women sipping latte with a blanket around them are too one dimensional . Anyone can do that.. RT is moving in the right direction. This is luxury lifestyle with scents and smells and travel (the 4 senses and the 4 corners of the earth/ world). not just blankets so be creative. I would love to see the opening shot as a lavender field , rose gardens, Eifle tower, Tuscany, Amalfi , Santorini, Swiss Alps, Bali SeaScapes, Pagoda gardens and bridges and dramatic places that excite and entice . BE Seductive yet inviting. Incorporate the finest materials, minerals, oils and elements from around the world

Taglines -

Experience the World together... and bring it HOME.

With Love and Serenity,
Lumo Pemberton Brandeis

Sites to link to as affiliate partners

Look at /vesko.example
include links to partners for upsell and selection of collaboration fragrances
www.oilvantia.example
www.innmarquee.example
www.odorelle.example
www.fumiworks.example
www.hollo.example
www. roamsandrafts.example

Also can you make the logo dynamic like someone is signing their name in real time and then draw the box after it? Play with the + sign. This entire site must also be coded and Shopify ready . Watch this YouTube video called Orbitude – Let the quiet hold you near and lets put LUMO logo handwritten over and instead of ORBITude

Thank you.
Really running of time and looking for artists and artistry versus static one dimensional templates. Be Creative and Magic!

Thanks LUMO

Really important is the the landing page has the animated signature of Lumo logo design exactly and not a new font. We want it to be LUMO and not a big BLANKET we want to downplay that . And then as they get into the CTO order and shopping cart exploration and her and inspiration story about us section etc have it look like a handwritten signature ending with

With Love and Serenity

Lumo Pemberton Brandeis - Kettering

Target Market(s)

All consumers. Influencers , Designers , Moms , Home owners, travelers , babies .

Industry/Entity Type

Wellness luxury blankets with

Coding

Coded - Design and coding required

Number of Pages Required

3 page

Font styles to use
Serif

Requirements
Must have
• See website examples provided . Visual , chic , design and world iconic luxury
Should not have
• Cheesy , boring ,

```html
<!DOCTYPE html>
<html lang="en">
<head>
<meta charset="utf-8">
<title>Lumo Throw Co</title>
<link href="https://fonts.googleapis.com/css2?family=Marcellus&family=Roboto:wght@400;500;700&display=swap" rel="stylesheet">
<style>
:root{
  --ink:#000;
  --paper:#fff;
  --text:#2b2b2b;
  --muted:#555;
  --line:#d9d9d9;
  --star:#f5a623;
  --soft:#f3f3f3;
}
*{box-sizing:border-box;margin:0;padding:0}
html,body{width:1200px;height:3334px;overflow:hidden;background:var(--paper)}
body{font-family:'Roboto',sans-serif;color:var(--text);position:relative}
.page{position:relative;width:1200px;height:3334px}
.abs{position:absolute}
.serif{font-family:'Marcellus',serif;font-weight:400}

.topbar{left:0;top:0;width:1200px;height:40px;background:var(--ink);color:var(--paper);font-size:13px;display:flex;align-items:center;justify-content:center}
.brand{display:flex;align-items:center;gap:10px;font-family:'Marcellus',serif;font-size:26px;color:var(--ink)}
.brand .mark{width:14px;height:14px;border:2px solid currentColor}
.header-brand{left:142px;top:70px}
.nav{left:523px;top:80px;display:flex;gap:34px;font-size:15px;color:#333}
.nav a{color:inherit;text-decoration:none;position:relative}
.nav a.active::after{content:"";position:absolute;left:0;right:0;bottom:-13px;height:3px;background:var(--ink)}
.icons{top:84px;left:986px;display:flex;gap:43px}

.hero{left:0;top:144px;width:1200px;height:520px;background:linear-gradient(100deg,#d9d6d0 0%,#c9c4bb 35%,#e3dccf 60%,#b9ada0 100%)}
.hero-box{left:97px;top:233px;width:593px;height:289px;border:8px solid var(--ink);background:rgba(255,255,255,.9);text-align:center;padding-top:42px}
.hero-box h1{font-family:'Marcellus',serif;font-weight:400;font-size:42px;line-height:40px;color:#111}
.hero-box p{font-size:13px;line-height:23px;margin:14px 30px 0;color:#222}
.btn{display:inline-block;background:var(--ink);color:var(--paper);font-weight:700;font-size:13px;padding:12px 32px;margin-top:14px}
.arrow-btn{width:43px;height:43px;border-radius:50%;background:rgba(50,50,50,.75);display:flex;align-items:center;justify-content:center}

.section-title{font-family:'Marcellus',serif;font-size:30px;color:#111}
.card{width:201px;height:215px;border:3px solid var(--line);border-radius:8px;background:var(--paper)}
.card .ph{position:absolute;left:20px;top:22px;right:20px;bottom:22px;border-radius:6px}
.card-featured{height:305px}
.product-name{width:201px;text-align:center;font-weight:700;font-size:15px;color:#111}
.price{width:201px;text-align:center;font-size:19px;color:#555}
.stars{width:201px;text-align:center;color:var(--star);font-size:14px;letter-spacing:2px}

.purpose{left:144px;top:1178px;width:912px;height:359px;background:linear-gradient(90deg,#5a4d42 0%,#6e6860 45%,#8c8a85 100%)}
.purpose-box{left:190px;top:1230px;width:393px;height:255px;border:3px solid var(--paper);background:rgba(60,55,50,.35);color:var(--paper);text-align:center;padding:18px 38px 0}
.purpose-box h2{font-family:'Marcellus',serif;font-weight:400;font-size:30px;line-height:40px}
.purpose-box p{font-size:13px;line-height:24px;text-align:justify;text-align-last:center}

.tile{width:286px;height:228px}
.tile-caption{width:286px;text-align:center;font-size:15px;color:#333;display:flex;justify-content:center;gap:22px;align-items:center}

.story{left:0;top:1930px;width:1200px;height:359px;background:var(--ink);color:var(--paper)}
.story h2{left:142px;top:50px;font-family:'Marcellus',serif;font-weight:400;font-size:30px;color:var(--paper)}
.story p{left:143px;top:105px;width:466px;font-size:16.5px;line-height:25.7px;text-align:justify}
.story .ph{left:720px;top:21px;width:318px;height:316px}

.news-card{left:457px;top:2438px;width:286px;height:306px;border:3px solid var(--ink);background:var(--soft);padding:20px 28px}
.news-card h3{font-family:'Marcellus',serif;font-weight:400;font-size:18px;line-height:24px;color:#111}
.news-card p{font-size:12.5px;line-height:20px;color:#666;margin-top:10px}
.news-card .more{margin-top:10px;font-size:13px;font-weight:500;color:#111;display:flex;gap:8px;align-items:center}

.footer{left:0;top:2854px;width:1200px;height:480px;background:var(--ink);color:var(--paper)}
.footer h4{font-family:'Marcellus',serif;font-weight:400;font-size:23px}
.links{list-style:none;font-size:15px;line-height:24px}
.footer-brand{color:var(--paper);font-size:30px}
.email{left:142px;top:315px;width:366px;height:46px;border:1px solid #aaa;display:flex;align-items:center;justify-content:space-between;padding:0 20px;font-size:14px}
.social{width:46px;height:46px;border-radius:50%;border:1px solid #555;display:flex;align-items:center;justify-content:center}
.social.on{background:var(--paper);border-color:var(--paper)}
.copy{left:0;top:3282px;width:1200px;text-align:center;font-size:15px}
</style>
</head>
<body>
<div class="page">

  <div class="abs topbar">Free shipping on all orders over $70</div>

  <div class="abs brand header-brand"><span class="mark"></span>Lumo Throw Co</div>
  <nav class="abs nav">
    <a class="active">Home</a><a>About</a><a>Product</a><a>Blog</a><a>Contact</a>
  </nav>
  <div class="abs icons">
    <svg width="12" height="12" viewBox="0 0 12 12"><circle cx="5" cy="5" r="3.8" fill="none" stroke="#111" stroke-width="1.8"/><line x1="7.8" y1="7.8" x2="11" y2="11" stroke="#111" stroke-width="2"/></svg>
    <svg width="13" height="12" viewBox="0 0 13 12"><path d="M0 1h2.5l1.8 6h7l1.5-4.5H3.5" fill="none" stroke="#111" stroke-width="1.6"/><circle cx="5" cy="10" r="1.3" fill="#111"/><circle cx="10" cy="10" r="1.3" fill="#111"/></svg>
  </div>

  <div class="abs hero" role="img" aria-label="Photo of a smiling woman wrapped in a cream knit throw holding a mug by a window"></div>
  <div class="abs hero-box">
    <h1>The Internet's<br>Softest Blanket</h1>
    <p>Lorem ipsum dolor sit amet, consectetur adipiscing elit, sed do eiusmod tempor incididunt ut labore et dolore magna aliqua.</p>
    <span class="btn">GET YOURS</span>
  </div>
  <div class="abs arrow-btn" style="left:552px;top:571px"><svg width="10" height="12"><path d="M7 1L2 6l5 5" fill="none" stroke="#fff" stroke-width="1.6"/></svg></div>
  <div class="abs arrow-btn" style="left:605px;top:571px"><svg width="10" height="12"><path d="M3 1l5 5-5 5" fill="none" stroke="#fff" stroke-width="1.6"/></svg></div>

  <h2 class="abs section-title" style="left:142px;top:742px">Meet Our Bestsellers</h2>

  <div class="abs card" style="left:141px;top:795px"><div class="ph" role="img" aria-label="Product photo of rolled throws in brown, cream, blue and grey" style="background:radial-gradient(circle,#c9a37c 0%,#e6ddd3 55%,#fff 80%)"></div></div>
  <div class="abs card card-featured" style="left:379px;top:795px"><div class="ph" role="img" aria-label="Product photo of a stack of folded knit blankets in grey and blue" style="bottom:110px;background:radial-gradient(circle,#7b8fb6 0%,#ccd4e2 55%,#fff 80%)"></div></div>
  <div class="abs card" style="left:619px;top:795px"><div class="ph" role="img" aria-label="Product photo of a folded white duvet" style="background:radial-gradient(circle,#e4e6ea 0%,#f3f4f6 55%,#fff 80%)"></div></div>
  <div class="abs card" style="left:857px;top:795px"><div class="ph" role="img" aria-label="Product photo of a folded pink knit throw" style="background:radial-gradient(circle,#c97b8c 0%,#ead2d7 55%,#fff 80%)"></div></div>

  <div class="abs stars" style="left:379px;top:995px">★★★★★</div>
  <div class="abs product-name" style="left:141px;top:1020px">Lorem ipsum dolor</div>
  <div class="abs product-name" style="left:379px;top:1020px">Lorem ipsum dolor</div>
  <div class="abs product-name" style="left:619px;top:1020px">Lorem ipsum dolor</div>
  <div class="abs product-name" style="left:857px;top:1020px">Lorem ipsum dolor</div>
  <div class="abs price" style="left:141px;top:1054px">From $ 10.00</div>
  <div class="abs price" style="left:379px;top:1054px">From $ 10.00</div>
  <div class="abs price" style="left:619px;top:1054px">From $ 10.00</div>
  <div class="abs price" style="left:857px;top:1054px">From $ 10.00</div>

  <div class="abs purpose" role="img" aria-label="Dim photo of a cream knit blanket on a rug with a green plant"></div>
  <div class="abs purpose-box">
    <h2>Blankets With<br>a Purpose</h2>
    <p>Lumo + Throw Co is the original and only “scented” luxury &amp; travel blanket company in the world introducing refillable infused and scented LuMo pearls (TM) Patent pending (ceramic beads) and Lumo “BRISK” cards (TM) combined with essential oils with medicinal life giving benefits .</p>
  </div>

  <div class="abs tile" role="img" aria-label="Photo of hands holding a tall stack of knit blankets" style="left:144px;top:1597px;background:linear-gradient(180deg,#e6e2dc,#a9a7a3)"></div>
  <div class="abs tile" role="img" aria-label="Photo of a woman in a white robe by a turquoise sea taking a photo" style="left:457px;top:1597px;background:linear-gradient(180deg,#8fc1d6,#3fa7b4 55%,#e9eef2)"></div>
  <div class="abs tile" role="img" aria-label="Photo of two women cuddled in a beige blanket on a sofa" style="left:770px;top:1597px;background:linear-gradient(180deg,#d7dbd6,#8e7a6a 60%,#cfc6bb)"></div>
  <div class="abs tile-caption" style="left:144px;top:1844px">Lorem ipsum dolor <svg width="14" height="12"><path d="M0 6h11M7 1l5 5-5 5" fill="none" stroke="#111" stroke-width="2.2"/></svg></div>
  <div class="abs tile-caption" style="left:457px;top:1844px">Lorem ipsum dolor <svg width="14" height="12"><path d="M0 6h11M7 1l5 5-5 5" fill="none" stroke="#111" stroke-width="2.2"/></svg></div>
  <div class="abs tile-caption" style="left:770px;top:1844px">Lorem ipsum dolor <svg width="14" height="12"><path d="M0 6h11M7 1l5 5-5 5" fill="none" stroke="#111" stroke-width="2.2"/></svg></div>

  <section class="abs story">
    <h2 class="abs">Our Story</h2>
    <p class="abs">Founded and inspired by Mirela aka “LUMO” Brandeis Kettering affectionately know by her hubby as “Super M “ , Mirela was nicknamed Lumo at birth and her brothers teased her to tears in her formative years giving her the nickname Lumo Pemberton . A college graduate in Health and wellness , fast forward, 5 kids later , Mirel now travels the world as a top travel influencer and consultant agent with Roams and Rafts luxury Travel www.Roamsandrafts.example .</p>
    <div class="abs ph" role="img" aria-label="Photo of a woman with glasses and a mug sitting under a cream knit blanket" style="background:linear-gradient(160deg,#e8e8e6,#b8b5b0 55%,#d9d6d0)"></div>
  </section>

  <h2 class="abs section-title" style="left:142px;top:2376px">Latest News</h2>
  <div class="abs tile" role="img" aria-label="Photo of a woman on a bed with a phone and a glass of wine" style="left:144px;top:2438px;height:306px;background:linear-gradient(170deg,#cfc9c2,#8a8580 50%,#4d5f6c)"></div>
  <div class="abs news-card">
    <h3>Lorem ipsum dolor sit amet, consectetur adipiscing elit</h3>
    <p>Lorem ipsum dolor sit amet, consectetur adipiscing elit, sed do eiusmod tempor incididunt ut labore et dolore magna aliqua. Ut enim ad minim veniam, quis nostrud exercitation ullamco laboris nisi ut aliquip ex ea commodo consequat.</p>
    <div class="more">Learn More <svg width="13" height="11"><path d="M0 5.5h10M6 1l5 4.5L6 10" fill="none" stroke="#111" stroke-width="2"/></svg></div>
  </div>
  <div class="abs tile" role="img" aria-label="Photo of a woman in a blue shirt sleeping on white sheets" style="left:770px;top:2438px;height:306px;background:linear-gradient(170deg,#eeeceb,#4f78a6 55%,#dcdad8)"></div>

  <footer class="abs footer">
    <h4 class="abs" style="left:142px;top:76px">Quick Links</h4>
    <ul class="abs links" style="left:142px;top:119px">
      <li>Home</li><li>About</li><li>Services</li><li>Blog</li><li>Contact</li>
    </ul>
    <h4 class="abs" style="left:374px;top:82px">Our Mission</h4>
    <p class="abs" style="left:374px;top:130px;width:320px;font-size:13px;line-height:20px">Lorem ipsum dolor sit amet, consectetur adipiscing elit, sed do eiusmod tempor incididunt ut labore et dolore magna aliqua.</p>
    <div class="abs brand footer-brand" style="left:790px;top:105px"><span class="mark"></span>Lumo Throw Co</div>
    <h4 class="abs" style="left:142px;top:272px">We Send Delicious Emails.</h4>
    <div class="abs email"><span>Email</span><svg width="13" height="11"><path d="M0 5.5h10M6 1l5 4.5L6 10" fill="none" stroke="#fff" stroke-width="2"/></svg></div>
    <div class="abs social" style="left:896px;top:311px"><svg width="12" height="12"><rect x="1" y="1" width="10" height="10" fill="none" stroke="#fff"/></svg></div>
    <div class="abs social on" style="left:952px;top:311px"><svg width="12" height="12"><circle cx="6" cy="6" r="4.5" fill="none" stroke="#111"/></svg></div>
    <div class="abs social" style="left:1007px;top:311px"><svg width="12" height="12"><rect x="1" y="2" width="10" height="8" rx="2" fill="none" stroke="#fff"/></svg></div>
    <div class="abs copy" style="top:428px">© Copyrights 2024 | All Rights Reserved</div>
  </footer>

</div>
</body>
</html>
```